Coastal Bright Sweep Business Card

We are a cleaning and waste management company with the slogan "making waste to landfill a thing of the past". We would like a re-design of our current business card. On the front we want to continue to use our logo as the focus point. On the back, we want the whole thing re-done to be less busy. We want the staff member’s name, the job title, mobile number, email and website. We do not want the address on the card. We still want the green, black and blue colours used, but a new font for the information on the back. Please do not change the logo design at all. We are also thinking about using icons to replace the text ‘mobile, email, website’. The “events + commercial” banner needs to be incorporated somewhere and needs to read “events + commercial + waste”. Another important point for consideration is that we are very concerned about being environmentally sustainable and will be printing on recycled paper. All designs should be made to compliment this in regards to boldness and colouring. Please find attached our logo, our colour chart and an image of our current business card.

```html
<!DOCTYPE html>
<html lang="en">
<head>
<meta charset="utf-8">
<title>Coastal Bright Sweep Business Card</title>
<link href="https://fonts.googleapis.com/css2?family=Source+Sans+3:wght@400;600;700&display=swap" rel="stylesheet">
<style>
  :root {
    --backdrop: #9a9a9a;
    --card-white: #ffffff;
    --card-black: #000000;
    --navy: #123c6e;
    --sky: #1aa3e3;
    --ink: #111111;
    --rule: #c8c8c8;
  }
  * { margin: 0; padding: 0; box-sizing: border-box; }
  html, body {
    width: 1200px;
    height: 900px;
    overflow: hidden;
    background: var(--backdrop);
    font-family: "Source Sans 3", Arial, sans-serif;
  }
  .canvas { position: relative; width: 1200px; height: 900px; }
  .card {
    position: absolute;
    top: 170px;
    width: 347px;
    height: 560px;
    background: var(--card-white);
    text-align: center;
  }
  .card--details { left: 259px; }
  .card--brand { left: 631px; }

  .brand-name {
    position: absolute;
    left: 0;
    right: 0;
    font-weight: 700;
    font-size: 50px;
    line-height: 1;
    letter-spacing: -0.5px;
  }
  .card--details .brand-name { top: 60px; color: var(--navy); }

  .staff-name {
    position: absolute;
    top: 354px;
    left: 0; right: 0;
    font-size: 22px;
    font-weight: 600;
    color: var(--navy);
    letter-spacing: 0.3px;
  }
  .staff-role {
    position: absolute;
    top: 382px;
    left: 0; right: 0;
    font-size: 15px;
    color: var(--ink);
  }
  .divider {
    position: absolute;
    top: 414px;
    left: 107px;
    width: 134px;
    height: 1px;
    background: var(--rule);
  }
  .contact-list {
    position: absolute;
    top: 432px;
    left: 0; right: 0;
    list-style: none;
    font-size: 15px;
    line-height: 23px;
    color: var(--ink);
  }
  .contact-label { color: var(--sky); font-weight: 600; }

  .brand-panel {
    position: absolute;
    top: 0; left: 0;
    width: 100%;
    height: 373px;
    background: var(--card-black);
  }
  .brand-panel .brand-name { top: 80px; color: var(--card-white); }

  .service-list {
    position: absolute;
    top: 398px;
    left: 0; right: 0;
    list-style: none;
    font-size: 31px;
    font-weight: 600;
    line-height: 48px;
    color: var(--ink);
  }
</style>
</head>
<body>
<main class="canvas">
  <section class="card card--details">
    <h1 class="brand-name">Coastal<br>Bright<br>Sweep</h1>
    <h2 class="staff-name">MORGAN TELLWRIGHT</h2>
    <p class="staff-role">Client Manager</p>
    <div class="divider"></div>
    <ul class="contact-list">
      <li><span class="contact-label">M</span>: 0400 555 218</li>
      <li><span class="contact-label">E</span>: mtellwright@coastalbrightsweep.com.au</li>
      <li><span class="contact-label">W</span>: www.coastalbrightsweep.com.au</li>
    </ul>
  </section>

  <section class="card card--brand">
    <div class="brand-panel">
      <p class="brand-name">Coastal<br>Bright<br>Sweep</p>
    </div>
    <ul class="service-list">
      <li>Events</li>
      <li>Commercial</li>
      <li>Waste</li>
    </ul>
  </section>
</main>
</body>
</html>
```